Plumbing company needs Business Card Design

Hi I need business card design based on logo which I uploaded. Its plumbing and heating company called Kranex Usługi Hydrauliczno-Gazowe. I want to see on my card motto of my company which is "...od wymiany uszczelki po wymiane łazienki.", my phone number, name, and website: 617248390, Marek Kowalczyk, info@kranex.org, www.kranex.org
I want to see logos of companys which I'm approved installer (Termolux) (La Valmont) (Corvo) (Pluma).
I want new creative look of business card. I like rounded corners.
Any questions please send message.
Thanks for intrest.
Business
Contact Information for Business Card
Marek Kowalczyk
617 248 390
info@kranex.org
www.kranex.org
...od wymiany uszczelki po wymiane łazienki.

```html
<!DOCTYPE html>
<html lang="pl">
<head>
<meta charset="UTF-8">
<title>Kranex – wizytówka</title>
<link rel="stylesheet" href="https://fonts.googleapis.com/css2?family=Noto+Sans:wght@400;700&family=Oswald:wght@500&display=swap">
<style>
  :root {
    --bg-top: #5e5e5e;
    --bg-bottom: #2f2f2f;
    --red: #e41f26;
    --yellow: #f6ef24;
    --navy: #203a7c;
    --blue: #1f5bb0;
    --ink: #111111;
    --white: #ffffff;
  }
  * { margin: 0; padding: 0; box-sizing: border-box; }
  html, body { width: 1200px; height: 900px; overflow: hidden; }
  body {
    position: relative;
    background: radial-gradient(ellipse at 30% 20%, var(--bg-top), var(--bg-bottom) 75%);
    font-family: "Noto Sans", Arial, sans-serif;
  }
  .card {
    position: absolute;
    border-radius: 42px;
    overflow: hidden;
    box-shadow: 0 6px 14px rgba(0,0,0,.45);
  }
  /* front */
  .card-front {
    left: 95px; top: 210px; width: 480px; height: 478px;
    background: var(--red);
  }
  .card-front .panel {
    position: absolute; left: 22px; top: 22px; right: 22px; bottom: 22px;
    background: var(--yellow);
    border-radius: 34px;
    display: flex; align-items: center; justify-content: center;
  }
  .front-name {
    font-weight: 700; font-size: 84px; color: var(--navy);
  }
  /* back */
  .card-back {
    left: 600px; top: 212px; width: 475px; height: 474px;
    background: var(--white);
  }
  .card-back svg.deco { position: absolute; left: 0; top: 0; }
  .brand {
    position: absolute; left: 38px; top: 62px;
    display: flex; align-items: center; gap: 16px;
  }
  .brand-square {
    width: 122px; height: 122px; border-radius: 12px;
    background: var(--yellow); border: 7px solid var(--red);
  }
  .brand-text { display: flex; flex-direction: column; }
  .brand-name {
    font-weight: 700; font-size: 64px; line-height: 1; color: var(--red);
  }
  .brand-tagline {
    font-family: "Oswald", "Arial Narrow", sans-serif;
    font-weight: 500; font-size: 21px; color: var(--navy); margin-top: 8px;
  }
  .motto {
    position: absolute; left: 0; right: 0; top: 205px;
    text-align: center; color: var(--red); font-size: 20px; line-height: 28px;
  }
  .person {
    position: absolute; left: 48px; top: 296px;
  }
  .person-first { font-size: 31px; color: var(--ink); line-height: 38px; }
  .person-last { font-size: 26px; color: var(--blue); line-height: 34px; margin-left: -4px; }
  .contact {
    position: absolute; left: 236px; top: 305px;
    font-size: 27px; color: var(--ink); line-height: 32px;
  }
  .contact-row { display: flex; align-items: center; gap: 6px; }
  .contact-row svg { flex: none; }
  .email { font-size: 24px; }
  .website {
    position: absolute; left: 0; right: 0; top: 437px;
    text-align: center; font-size: 22px; color: var(--blue);
  }
</style>
</head>
<body>
  <section class="card card-front">
    <div class="panel">
      <span class="front-name">Kranex</span>
    </div>
  </section>

  <section class="card card-back">
    <svg class="deco" width="475" height="474" viewBox="0 0 475 474" aria-hidden="true">
      <polygon points="0,0 475,0 475,30 455,30 445,2 0,2" fill="var(--red)"/>
      <rect x="0" y="0" width="475" height="30" fill="var(--red)"/>
      <polygon points="0,266 475,266 475,433 0,433" fill="var(--yellow)"/>
      <polygon points="0,266 50,266 20,393 150,393 0,428" fill="var(--red)"/>
      <line x1="218" y1="298" x2="218" y2="390" stroke="var(--red)" stroke-width="2"/>
    </svg>

    <div class="brand">
      <div class="brand-square"></div>
      <div class="brand-text">
        <span class="brand-name">Kranex</span>
        <span class="brand-tagline">Usługi Hydrauliczno-Gazowe</span>
      </div>
    </div>

    <p class="motto">Od wymiany uszczelki<br>po wymiane łazienki</p>

    <div class="person">
      <div class="person-first">Marek</div>
      <div class="person-last">Kowalczyk</div>
    </div>

    <div class="contact">
      <div class="contact-row">
        <svg width="12" height="14" viewBox="0 0 12 14"><path d="M2 1 L5 1 L6 4 L4 5 C5 8 6 9 8 10 L9 8 L12 9 L12 12 C8 13 1 7 2 1Z" fill="var(--blue)"/></svg>
        <span>617.248.390</span>
      </div>
      <div class="contact-row email">
        <svg width="10" height="8" viewBox="0 0 10 8"><rect width="10" height="8" fill="var(--blue)"/></svg>
        <span>info@kranex.org</span>
      </div>
    </div>

    <div class="website">www.kranex.org</div>
  </section>
</body>
</html>
```